Harmonies of the Coast Presents

Show name:
Maple Chorus Revue
Location:
Larkwood High School
4286 Fernhollow Rd, Citrus Heights, CA 95617
Times: 2 p.m. & 7 p.m.
Special Guests:
Bright Chord
Harbor Quartet
Copperleaf Five
Ticket Prices:
VIP $35.00
General $25.00
Student $15.00

```html
<!DOCTYPE html>
<html lang="en">
<head>
<meta charset="utf-8">
<title>Maple Chorus Revue</title>
<link rel="stylesheet" href="https://fonts.googleapis.com/css2?family=Anton&family=Figtree:wght@500;600;700;800&family=Norican&display=swap">
<style>
  :root {
    --backdrop: #6b6b6d;
    --paper: #fdfcfa;
    --pink: #e0158a;
    --purple: #6a1fa8;
    --green: #14934a;
    --ink: #2a2230;
    --gold: #f4c46a;
  }
  * { margin: 0; padding: 0; box-sizing: border-box; }
  html, body { width: 1200px; height: 1200px; overflow: hidden; background: var(--backdrop); }
  .poster {
    position: absolute; left: 191px; top: 21px;
    width: 843px; height: 1193px;
    transform: scale(0.97); transform-origin: top left;
    background: linear-gradient(to bottom, var(--paper) 0%, #fdf9f2 60%, #fbe9c4 85%, var(--gold) 100%);
    overflow: hidden;
    font-family: "Figtree", sans-serif; color: var(--ink);
  }
  .art { position: absolute; }
  .art-birds {
    left: 450px; top: 0; width: 393px; height: 460px;
    background: radial-gradient(ellipse at 60% 50%, rgba(214,96,120,.55) 0%, rgba(240,170,120,.35) 45%, rgba(253,252,250,0) 72%);
  }
  .art-notes {
    left: 370px; top: 480px; width: 473px; height: 240px;
    background: radial-gradient(ellipse at 55% 50%, rgba(236,90,110,.35) 0%, rgba(150,120,220,.2) 45%, rgba(253,252,250,0) 72%);
  }
  .art-photo {
    left: 380px; top: 700px; width: 463px; height: 493px;
    background: radial-gradient(ellipse at 55% 55%, rgba(232,205,190,.9) 0%, rgba(240,214,160,.7) 40%, rgba(244,196,106,.0) 75%),
                linear-gradient(to bottom, rgba(253,249,242,0) 0%, rgba(225,190,110,.7) 100%);
  }
  .brand {
    position: absolute; left: 48px; top: 82px;
    font-weight: 600; font-size: 40px; color: var(--purple);
  }
  .title-script {
    position: absolute; left: 44px; top: 182px;
    font-family: "Norican", cursive; font-size: 104px; line-height: 1.1; white-space: nowrap;
  }
  .title-script .pink { color: var(--pink); }
  .title-script .purple { color: var(--purple); }
  .title-block {
    position: absolute; left: 48px; top: 310px;
    font-family: "Anton", sans-serif; font-size: 80px; line-height: 1; color: var(--green);
  }
  .date-day, .date-full {
    position: absolute; left: 48px;
    font-family: "Anton", sans-serif; font-size: 48px; line-height: 1;
  }
  .date-day { top: 444px; color: var(--pink); }
  .date-full { top: 505px; color: var(--purple); }
  .times {
    position: absolute; left: 48px; top: 560px;
    font-weight: 800; font-size: 36px; color: var(--pink);
  }
  .label { font-weight: 800; font-size: 22px; color: var(--purple); text-transform: uppercase; }
  .location { position: absolute; left: 48px; top: 637px; }
  .venue { font-weight: 700; font-size: 24px; margin-top: 4px; text-transform: uppercase; }
  .address { font-weight: 500; font-size: 20px; line-height: 28px; width: 290px; }
  .guests { position: absolute; left: 48px; top: 808px; }
  .guest-list { list-style: none; margin-top: 10px; }
  .guest-list li { display: flex; align-items: center; gap: 10px; font-weight: 500; font-size: 23px; height: 34px; }
  .guest-list svg { width: 17px; height: 17px; flex: none; }
  .tickets {
    position: absolute; left: 48px; top: 981px; width: 310px;
    border: 2px solid var(--purple); border-radius: 4px; overflow: hidden;
    border-collapse: separate; border-spacing: 0;
  }
  .tickets th {
    background: var(--purple); color: #fff; font-weight: 800; font-size: 21px;
    height: 36px; text-transform: uppercase;
  }
  .tickets td { height: 34px; font-size: 20px; border-top: 1px solid var(--purple); }
  .tickets td.tier { font-weight: 700; padding-left: 10px; width: 155px; border-right: 1px solid var(--purple); text-transform: uppercase; }
  .tickets td.price { text-align: center; font-weight: 500; }
  .website {
    position: absolute; left: 48px; top: 1142px;
    font-weight: 700; font-size: 20px; color: var(--purple);
  }
</style>
</head>
<body>
  <main class="poster">
    <div class="art art-birds" role="img" aria-label="Watercolour songbirds perched on a blossoming branch with falling petals"></div>
    <div class="art art-notes" role="img" aria-label="Colourful treble clef, musical notes and butterflies"></div>
    <div class="art art-photo" role="img" aria-label="Photo of a young girl with arms raised in a sunlit flower meadow"></div>

    <div class="brand">Harmonies of the Coast</div>

    <h1 class="title-script"><span class="pink">Maple</span> <span class="purple">Chorus</span></h1>
    <div class="title-block">REVUE</div>

    <div class="date-day">SATURDAY,</div>
    <div class="date-full">APRIL 23, 2022</div>
    <div class="times">2 P.M. &amp; 7 P.M.</div>

    <section class="location">
      <div class="label">Location:</div>
      <div class="venue">Larkwood High School</div>
      <div class="address">4286 Fernhollow Rd, Citrus Heights, CA 95617</div>
    </section>

    <section class="guests">
      <div class="label">Special Guests:</div>
      <ul class="guest-list">
        <li><svg viewBox="0 0 16 16"><circle cx="8" cy="8" r="8" fill="#e0158a"/><path d="M4.5 8.2l2.3 2.3 4.7-4.7" stroke="#fff" stroke-width="2" fill="none"/></svg>Bright Chord</li>
        <li><svg viewBox="0 0 16 16"><circle cx="8" cy="8" r="8" fill="#e0158a"/><path d="M4.5 8.2l2.3 2.3 4.7-4.7" stroke="#fff" stroke-width="2" fill="none"/></svg>Harbor Quartet</li>
        <li><svg viewBox="0 0 16 16"><circle cx="8" cy="8" r="8" fill="#e0158a"/><path d="M4.5 8.2l2.3 2.3 4.7-4.7" stroke="#fff" stroke-width="2" fill="none"/></svg>Copperleaf Five</li>
      </ul>
    </section>

    <table class="tickets">
      <tr><th colspan="2">Ticket Prices:</th></tr>
      <tr><td class="tier">VIP</td><td class="price">$35.00</td></tr>
      <tr><td class="tier">General</td><td class="price">$25.00</td></tr>
      <tr><td class="tier">Student</td><td class="price">$15.00</td></tr>
    </table>

    <div class="website">www.harmoniesofthecoast.org</div>
  </main>
</body>
</html>
```